Etiketten für Bio Seifen
Zielgruppe
Wir stellen hochwertig 'handgemachte' Bio-Seifen her. Die Zielgruppe ist von 3-99 Jahren und zusätzlich haben wir auch noch Seife für Hunde.
Der Firmenname ist 'Kestrima'
Aufgabenstellung
Das Etikett soll Bezug auf Natur, Bio, Nachhaltigkeit nehmen. Wir stellen uns 'weiche' Aquarellfarben vor...Seife: Lavendel, Calendular, 7 Kräuter etc.
Das Etikett soll auf eine Beutelschachtel. Die Schachtel hat eine Anmaße: Breite 55mm; Höhe 120mm; Tiefe 30mm
Das Etikett soll im vorderen- und hinteren Bereich zusammenhängend geklebt werden.
Das Etikett soll eine Abmaße von: Breite 51mm; Höhe 114mm haben (Vorderseite) Rückseite gleich.
Wir möchten die Produkte auch gerne nummerieren, d.h. jede Seife hat eine Nummer die nicht zu groß dargestellt werden soll aber trotzdem gut leserlich.
Wir haben noch ein paar Bilder hochgeladen wie wir uns das ungefähr vorstellen.

```html
<!DOCTYPE html>
<html lang="de">
<head>
<meta charset="utf-8">
<title>Kestrima – Handgemachte Seife Lavendel</title>
<link rel="stylesheet" href="https://fonts.googleapis.com/css2?family=Montserrat:wght@500;600;700&family=Kaushan+Script&display=swap">
<style>
  :root {
    --teal: #3a9686;
    --mint-soft: #cdeee0;
    --paper: #ffffff;
    --inner-line: #e4e6e6;
    --blush: #f6c9c0;
    --coral: #ef7b72;
    --mint: #bfe8d4;
    --lemon: #eef0a6;
    --lavender: #b8a6ea;
  }
  * { margin: 0; padding: 0; box-sizing: border-box; }
  html, body {
    width: 1200px;
    height: 2681px;
    overflow: hidden;
    background: var(--paper);
  }
  .label {
    position: relative;
    width: 1200px;
    height: 2681px;
    overflow: hidden;
  }
  .floral-background {
    position: absolute;
    inset: 0;
    background:
      radial-gradient(circle at 20% 22%, var(--blush) 0, transparent 22%),
      radial-gradient(circle at 55% 12%, var(--lemon) 0, transparent 18%),
      radial-gradient(circle at 90% 12%, var(--coral) 0, transparent 12%),
      radial-gradient(circle at 38% 20%, var(--lavender) 0, transparent 14%),
      radial-gradient(circle at 75% 32%, var(--coral) 0, transparent 13%),
      radial-gradient(circle at 8% 70%, var(--coral) 0, transparent 12%),
      radial-gradient(circle at 92% 70%, var(--blush) 0, transparent 18%),
      radial-gradient(circle at 60% 88%, var(--blush) 0, transparent 16%),
      radial-gradient(circle at 30% 92%, var(--lemon) 0, transparent 14%),
      radial-gradient(circle at 85% 92%, var(--coral) 0, transparent 12%),
      linear-gradient(160deg, var(--mint) 0%, #f4fbf7 45%, var(--mint) 100%);
    opacity: 0.85;
  }
  .title-panel {
    position: absolute;
    left: 134px;
    top: 1220px;
    width: 926px;
    height: 887px;
    background: var(--paper);
    border: 3px solid var(--teal);
  }
  .title-panel::before {
    content: "";
    position: absolute;
    inset: 14px;
    border: 2px solid var(--inner-line);
  }
  .number-badge {
    position: absolute;
    left: 536px;
    top: 1164px;
    width: 120px;
    height: 120px;
    border-radius: 50%;
    background: var(--teal);
    color: var(--paper);
    font-family: "Montserrat", sans-serif;
    font-weight: 600;
    font-size: 40px;
    display: flex;
    align-items: center;
    justify-content: center;
    z-index: 2;
  }
  .panel-text {
    position: absolute;
    left: 134px;
    width: 926px;
    text-align: center;
    color: var(--teal);
    font-family: "Montserrat", sans-serif;
  }
  .product-type {
    top: 1350px;
    font-weight: 600;
    font-size: 46px;
    line-height: 62px;
    letter-spacing: 9px;
  }
  .scent-name {
    top: 1525px;
    font-family: "Kaushan Script", cursive;
    font-weight: 400;
    font-size: 130px;
    line-height: 180px;
  }
  .ornament-placeholder {
    position: absolute;
    left: 480px;
    top: 1712px;
    width: 270px;
    height: 170px;
    background: var(--mint-soft);
  }
  .brand-name {
    top: 1896px;
    font-weight: 700;
    font-size: 50px;
    line-height: 66px;
    letter-spacing: 12px;
  }
  .edition-year {
    top: 1992px;
    font-weight: 600;
    font-size: 44px;
    line-height: 66px;
    letter-spacing: 6px;
  }
</style>
</head>
<body>
  <main class="label">
    <div class="floral-background" role="img" aria-label="Aquarell-Blumenmuster mit Lavendelzweigen, rosa, roten und gelben Blüten und mintgrünen Blättern"></div>

    <section class="title-panel"></section>
    <div class="number-badge">No 7</div>

    <p class="panel-text product-type">HANDGEMACHTE<br>SEIFE</p>
    <h1 class="panel-text scent-name">Lavendel</h1>
    <div class="ornament-placeholder" role="img" aria-label="Platz für ein Aquarell-Ornament in Mintgrün"></div>
    <p class="panel-text brand-name">KESTRIMA</p>
    <p class="panel-text edition-year">2022</p>
  </main>
</body>
</html>
```